Card design for orthopaedic surgeons working as The Brindlewood Orthopaedic Centre

Business cards, letterhead

Colors

Designer to choose colors to be used in the design.

Requirements
Must have
• Late addition.
• Cards letterhead must have logos of
• Corvane Federated Institute of Surgeons
• Meridale Orthopaedic Society
Nice to have
• Back of card to have space for appointment time to be added by hand and some blank space for writing incidental other notes.

```html
<!DOCTYPE html>
<html lang="en">
<head>
<meta charset="utf-8">
<title>The Brindlewood Orthopaedic Centre – Stationery</title>
<link href="https://fonts.googleapis.com/css2?family=Montserrat:wght@400&family=Roboto:wght@400&family=Lato:wght@400;700&display=swap" rel="stylesheet">
<style>
  :root {
    --backdrop: #d9d9d9;
    --paper: #ffffff;
    --navy: #08304a;
    --navy-card: #05314a;
    --sky: #46a7df;
    --ink: #0f2a44;
    --white: #ffffff;
  }
  * { margin: 0; padding: 0; box-sizing: border-box; }
  html, body { width: 1200px; height: 1200px; overflow: hidden; }
  body { background: var(--backdrop); position: relative; }

  .sheet, .card {
    position: absolute;
    overflow: hidden;
    box-shadow: 2px 3px 8px rgba(0,0,0,0.28);
  }
  .wave { position: absolute; inset: 0; width: 100%; height: 100%; }

  .wordmark {
    position: absolute;
    font-family: "Montserrat", sans-serif;
    font-weight: 400;
    white-space: nowrap;
    letter-spacing: -0.02em;
  }

  /* Letterhead */
  .letterhead { left: 14px; top: 95px; width: 785px; height: 1009px; background: var(--paper); }
  .letterhead .wordmark { left: 66px; top: 98px; font-size: 27px; color: var(--ink); }
  .letterhead-contact {
    position: absolute; left: 58px; top: 917px;
    font-family: "Roboto", sans-serif; font-size: 12.5px; color: var(--white);
    list-style: none;
  }
  .letterhead-contact li { display: flex; align-items: center; height: 15.8px; }
  .letterhead-contact svg { width: 11px; height: 11px; margin-right: 7px; flex: none; }

  /* Business card front */
  .card { width: 367px; height: 213px; }
  .card-front { left: 819px; top: 368px; background: var(--paper); }
  .card-front .wordmark { right: 17px; top: 32px; font-size: 13px; color: var(--ink); }
  .card-details {
    position: absolute; left: 18px; top: 103px;
    font-family: "Lato", sans-serif; color: var(--white); font-size: 8.8px; line-height: 12px;
  }
  .card-name { font-weight: 700; font-size: 11px; color: var(--sky); letter-spacing: 0.02em; line-height: 13px; }
  .card-role { margin-bottom: 5px; }
  .card-address { margin-bottom: 5px; }
  .card-contact { list-style: none; }
  .card-contact li { display: flex; align-items: center; }
  .card-contact svg { width: 8px; height: 8px; margin-right: 5px; flex: none; }

  /* Business card back */
  .card-back { left: 819px; top: 619px; background: var(--navy-card); }
  .card-back .wordmark { left: 0; right: 0; top: 104px; text-align: center; font-size: 17px; color: var(--white); }
</style>
</head>
<body>

<section class="sheet letterhead" aria-label="Letterhead">
  <div class="wordmark">The Brindlewood Orthopaedic Centre</div>
  <svg class="wave" viewBox="0 0 1264 1624" preserveAspectRatio="none" aria-hidden="true">
    <path d="M0 1418 C 300 1385, 560 1440, 760 1512 C 900 1562, 1100 1612, 1264 1535 V1624 H0 Z" fill="var(--sky)"/>
    <path d="M0 1450 C 300 1410, 560 1462, 740 1532 C 880 1582, 1080 1622, 1264 1540 V1624 H0 Z" fill="var(--navy)" stroke="var(--white)" stroke-width="3"/>
  </svg>
  <ul class="letterhead-contact">
    <li><svg viewBox="0 0 24 24"><path fill="var(--sky)" d="M6.6 10.8a15.2 15.2 0 0 0 6.6 6.6l2.2-2.2c.3-.3.7-.4 1-.2 1.1.4 2.3.6 3.6.6.6 0 1 .4 1 1V20c0 .6-.4 1-1 1A17 17 0 0 1 3 4c0-.6.4-1 1-1h3.5c.6 0 1 .4 1 1 0 1.3.2 2.5.6 3.6.1.3 0 .7-.2 1z"/></svg>(555) 204-0187</li>
    <li><svg viewBox="0 0 24 24"><path fill="var(--sky)" d="M2 5h20v14H2z M2 5l10 8 10-8" stroke="var(--navy)" stroke-width="1.5"/></svg>info@websitename.com</li>
    <li><svg viewBox="0 0 24 24" fill="none" stroke="var(--sky)" stroke-width="2"><circle cx="12" cy="12" r="9"/><path d="M3 12h18M12 3c3 3 3 15 0 18M12 3c-3 3-3 15 0 18"/></svg>www.websitename.com</li>
    <li><svg viewBox="0 0 24 24" fill="none" stroke="var(--sky)" stroke-width="2"><path d="M12 22s7-7 7-12a7 7 0 0 0-14 0c0 5 7 12 7 12z"/><circle cx="12" cy="10" r="2.5"/></svg>418 Harlow Crest Rd. Fenmore, OH 45990</li>
  </ul>
</section>

<section class="card card-front" aria-label="Business card front">
  <div class="wordmark">The Brindlewood Orthopaedic Centre</div>
  <svg class="wave" viewBox="0 0 592 342" preserveAspectRatio="none" aria-hidden="true">
    <path d="M0 108 C 120 102, 220 130, 320 198 C 400 252, 470 285, 592 254 V342 H0 Z" fill="var(--sky)"/>
    <path d="M0 122 C 120 116, 220 142, 312 206 C 392 260, 470 290, 592 262 V342 H0 Z" fill="var(--navy-card)" stroke="var(--white)" stroke-width="2"/>
  </svg>
  <div class="card-details">
    <div class="card-name">DARREN WHITLOW</div>
    <div class="card-role">Owner</div>
    <div class="card-address">2716 Larkspur Street, Elmbrook<br>NC 2, United States</div>
    <ul class="card-contact">
      <li><svg viewBox="0 0 24 24"><path fill="var(--sky)" d="M6.6 10.8a15.2 15.2 0 0 0 6.6 6.6l2.2-2.2c.3-.3.7-.4 1-.2 1.1.4 2.3.6 3.6.6.6 0 1 .4 1 1V20c0 .6-.4 1-1 1A17 17 0 0 1 3 4c0-.6.4-1 1-1h3.5c.6 0 1 .4 1 1 0 1.3.2 2.5.6 3.6.1.3 0 .7-.2 1z"/></svg>000-000-000-000</li>
      <li><svg viewBox="0 0 24 24"><path fill="var(--sky)" d="M2 5h20v14H2z M2 5l10 8 10-8" stroke="var(--navy-card)" stroke-width="1.5"/></svg>info@websitename.com</li>
      <li><svg viewBox="0 0 24 24" fill="none" stroke="var(--sky)" stroke-width="2"><circle cx="12" cy="12" r="9"/><path d="M3 12h18M12 3c3 3 3 15 0 18M12 3c-3 3-3 15 0 18"/></svg>www.websitename.com</li>
    </ul>
  </div>
</section>

<section class="card card-back" aria-label="Business card back">
  <div class="wordmark">The Brindlewood Orthopaedic Centre</div>
</section>

</body>
</html>
```